Menu Edit

Hello. We need a pricing edit on our current menu and new logo swapped (we already have the new logo), as well as colour changes. Also, we require a takeaway menu, in-store menu and footpath a-frame edit as well. I have attached the files bellow.

```html
<!DOCTYPE html>
<html lang="en">
<head>
<meta charset="utf-8">
<title>Harbour Line Fish Grill – Menu Panels</title>
<link href="https://fonts.googleapis.com/css2?family=Montserrat:wght@400;500;700;800&family=Roboto+Slab:wght@700&display=swap" rel="stylesheet">
<style>
  :root {
    --backdrop: #e1e2e1;
    --paper: #ffffff;
    --ink: #111111;
    --coral: #e8432a;
    --faint: #e3e4e6;
  }
  * { box-sizing: border-box; margin: 0; padding: 0; }
  html, body { width: 1200px; height: 950px; overflow: hidden; }
  body {
    background: var(--backdrop);
    font-family: "Montserrat", sans-serif;
    color: var(--ink);
    position: relative;
  }
  .panel {
    position: absolute;
    top: 43px;
    width: 502px;
    height: 743px;
    background: var(--paper);
    box-shadow: 0 2px 8px rgba(0,0,0,0.18);
  }
  .panel--hours { left: 71px; }
  .panel--platters { left: 627px; }
  .panel > * { position: absolute; }
  .center { left: 0; right: 0; text-align: center; }

  .dots-top {
    top: 36px; left: 31px; width: 208px; height: 4px;
    background: radial-gradient(circle, var(--coral) 1.4px, transparent 1.8px) 0 0 / 9.9px 4px repeat-x;
  }
  .dots-side {
    left: 477px; top: 620px; width: 4px; height: 123px;
    background: radial-gradient(circle, var(--coral) 1.4px, transparent 1.8px) 0 0 / 4px 10px repeat-y;
  }
  .brand {
    top: 103px;
    font-weight: 800; font-size: 25px; letter-spacing: 0.3px;
    color: var(--ink);
    display: flex; justify-content: center; align-items: center; gap: 8px;
  }
  .brand-dot { width: 9px; height: 9px; border-radius: 50%; background: var(--coral); }

  .deco { border-radius: 50%; }
  .deco--lemon {
    left: 200px; top: 147px; width: 102px; height: 102px;
    border: 2px solid var(--faint);
    background: radial-gradient(circle, #f3f4f5 0%, #fafafa 70%, transparent 72%);
  }
  .deco--crab {
    left: 173px; top: 146px; width: 156px; height: 122px;
    background: radial-gradient(ellipse at center, #eceded 0%, #f5f5f6 55%, rgba(255,255,255,0) 72%);
  }
  .headline {
    font-family: "Roboto Slab", serif; font-weight: 700;
    color: var(--coral); line-height: 1;
  }
  .headline--hours { top: 176px; font-size: 48px; }
  .headline--platters { top: 184px; font-size: 41px; white-space: nowrap; }

  .hours { font-size: 21px; line-height: 27px; }
  .hours-row { display: block; }
  .hours b { font-weight: 800; margin-right: 10px; }
  .hours { top: 263px; }

  .rule { height: 1.5px; background: var(--coral); }
  .rule--hours { top: 339px; left: 40px; width: 422px; }
  .services { top: 358px; font-size: 21.5px; line-height: 29px; font-weight: 500; letter-spacing: 0.4px; }
  .byo { top: 452px; font-size: 14.5px; font-weight: 700; }
  .prep-box {
    top: 483px; left: 21px; width: 460px; height: 76px;
    border: 1.5px solid var(--coral); text-align: center;
  }
  .prep-title { margin-top: 13px; font-size: 18.5px; font-weight: 500; letter-spacing: 0.3px; }
  .prep-options { margin-top: 6px; font-size: 16px; font-weight: 500; }

  .phone {
    top: 613px; display: flex; justify-content: center; align-items: center; gap: 10px;
    font-weight: 800; font-size: 55px; color: var(--coral); letter-spacing: 1px; line-height: 1;
  }
  .phone svg { width: 52px; height: 42px; }
  .rule--foot { top: 683px; left: 40px; width: 422px; height: 1.5px; background: var(--ink); }
  .web { top: 690px; font-size: 21.5px; font-weight: 700; }

  .platter-list { top: 285px; left: 33px; width: 434px; list-style: none; }
  .platter-list li {
    height: 38px; border-bottom: 1.5px solid var(--coral);
    text-align: center; font-weight: 700; font-size: 18.5px; letter-spacing: 0.4px;
    line-height: 14px; padding-top: 0;
  }
  .platter-list li:first-child { height: 28px; }
  .includes-title { top: 439px; font-size: 18px; font-weight: 700; color: var(--coral); }
  .includes-text { top: 467px; left: 40px; right: 40px; font-size: 17.5px; line-height: 24px; }

  .note {
    position: absolute; top: 815px; left: 0; right: 0; text-align: center;
    font-family: "Roboto Slab", serif; font-weight: 700; font-size: 30px; line-height: 36.5px;
    color: #1b1b1b;
  }
</style>
</head>
<body>

<section class="panel panel--hours">
  <div class="dots-top"></div>
  <div class="brand center"><span>HARBOUR LINE FISH GRILL</span><span class="brand-dot"></span></div>
  <div class="deco deco--lemon" role="img" aria-label="Faint line illustration of a lemon slice"></div>
  <h1 class="headline headline--hours center">Open Every Day</h1>
  <p class="hours center">
    <span class="hours-row"><b>Mon – Thurs</b>5pm to 9pm</span>
    <span class="hours-row"><b>Fri – Sun</b>12pm to 9pm</span>
  </p>
  <div class="rule rule--hours"></div>
  <p class="services center">CASUAL DINING | TAKEAWAY<br>ONLINE ORDERING &amp; DELIVERY<br>FRESH RETAIL</p>
  <p class="byo center">BYO Welcome! Wine, Beer &amp; Spirits / Soft Drinks Available</p>
  <div class="prep-box">
    <p class="prep-title">Choose your preparation:</p>
    <p class="prep-options">PANKO CRUMBED / TEMPURA BATTERED / GRILLED</p>
  </div>
  <div class="phone center">
    <svg viewBox="0 0 52 42" aria-hidden="true"><path fill="#e8432a" d="M4 10c0-6 10-8 22-8s22 2 22 8v5h-10v-4c0-2-5-3-12-3s-12 1-12 3v4H4z"/><path fill="#e8432a" d="M16 14h20l10 12v14H6V26z"/><g fill="#fff"><rect x="19" y="24" width="3" height="3"/><rect x="24.5" y="24" width="3" height="3"/><rect x="30" y="24" width="3" height="3"/><rect x="19" y="29" width="3" height="3"/><rect x="24.5" y="29" width="3" height="3"/><rect x="30" y="29" width="3" height="3"/></g></svg>
    <span>3555 0142</span>
  </div>
  <div class="rule--foot"></div>
  <p class="web center">www.harbourlinefish.com.au</p>
  <div class="dots-side"></div>
</section>

<section class="panel panel--platters">
  <div class="dots-top"></div>
  <div class="brand center"><span>HARBOUR LINE FISH GRILL</span><span class="brand-dot"></span></div>
  <div class="deco deco--crab" role="img" aria-label="Faint line illustration of a crab"></div>
  <h1 class="headline headline--platters center">Cooked Seafood Platters</h1>
  <ul class="platter-list">
    <li>Cooked Platter for One</li>
    <li>Cooked Platter for Two</li>
    <li>Cooked Platter for Three</li>
  </ul>
  <p class="includes-title center">Cooked Seafood Platters include:</p>
  <p class="includes-text center">Queensland whiting, calamari, salt &amp; pepper calamari, ocean king prawns, sea scallops, beer battered chips, one of our freshly made salads, homemade tartare sauce, lemon &amp; parsley.</p>
  <div class="phone center">
    <svg viewBox="0 0 52 42" aria-hidden="true"><path fill="#e8432a" d="M4 10c0-6 10-8 22-8s22 2 22 8v5h-10v-4c0-2-5-3-12-3s-12 1-12 3v4H4z"/><path fill="#e8432a" d="M16 14h20l10 12v14H6V26z"/><g fill="#fff"><rect x="19" y="24" width="3" height="3"/><rect x="24.5" y="24" width="3" height="3"/><rect x="30" y="24" width="3" height="3"/><rect x="19" y="29" width="3" height="3"/><rect x="24.5" y="29" width="3" height="3"/><rect x="30" y="29" width="3" height="3"/></g></svg>
    <span>3555 0142</span>
  </div>
  <div class="rule--foot"></div>
  <p class="web center">www.harbourlinefish.com.au</p>
  <div class="dots-side"></div>
</section>

<p class="note">Here is the first menu.<br>Let me know if you like this<br>version to continue the other 2 menus</p>

</body>
</html>
```